Dog care service needs business card design

Our company is Paws Harbour. We provide care for dogs while their owners are away, either through home visits or a holiday stay in the homes of carefully selected minders. Our existing website & Chatterbook cover should provide all the colour cues for our business cards - namely blues, blondes and grey. We have an existing logo (provided).

www.pawsharbourcare.example.au
www.facebook.com/pawsharbourcareau

We wish to clearly communicate our three areas of service "dog minding, home visits, dog walking".

We would like to have the files ready for upload to Printlyne (or similar) for immediate printing.

Target Market(s)

Dog owners who love their dogs like family

Industry/Entity Type

Business

Contact Information for Business Card

Paws Harbour
Ph: 0417 358 904

Font styles to use
Sans Serif

Colors
33a6d7
3176b5

Requirements
Must have
• Logo
• Telephone number
• website
• "Dog minding, home visits, dog walking"
Should not have
• any additional illustrations beyond the logo.

```html
<!DOCTYPE html>
<html lang="en">
<head>
<meta charset="utf-8">
<title>Paws Harbour – Business Cards</title>
<link rel="stylesheet" href="https://fonts.googleapis.com/css2?family=Montserrat:wght@600&family=Open+Sans:wght@400;700&display=swap">
<style>
  :root {
    --sky: #33a6d7;
    --ocean: #3176b5;
    --navy: #2e3a4f;
    --white: #ffffff;
    --stage: #e9ecef;
    --photo-grass: linear-gradient(160deg, #9cc86a 0%, #5f8f3a 100%);
    --photo-door: linear-gradient(180deg, #e9e4dc 0%, #a9783f 100%);
    --photo-park: linear-gradient(180deg, #6f8f5a 0%, #3f7a34 100%);
  }
  * { box-sizing: border-box; margin: 0; padding: 0; }
  html, body { width: 1200px; height: 620px; overflow: hidden; }
  body {
    background: var(--stage);
    font-family: "Open Sans", Arial, sans-serif;
    position: relative;
  }
  .card {
    position: absolute;
    top: 155px;
    width: 540px;
    height: 310px;
    background: var(--white);
    overflow: hidden;
    box-shadow: 0 6px 18px rgba(0,0,0,.18);
  }
  .card--front { left: 40px; }
  .card--back { left: 620px; }

  .band {
    position: absolute;
    left: 0; right: 0; bottom: 0;
    background: var(--sky);
  }
  .card--front .band { top: 235px; }
  .card--back .band { top: 150px; }

  .brand {
    position: absolute;
    display: flex;
    align-items: center;
    gap: 14px;
  }
  .brand__dot {
    width: 52px; height: 52px;
    border-radius: 50%;
    background: var(--ocean);
  }
  .brand__name {
    font-family: "Montserrat", Arial, sans-serif;
    font-weight: 600;
    font-size: 34px;
    color: var(--navy);
    line-height: 1;
  }
  .card--front .brand { left: 62px; top: 112px; }
  .card--back .brand { left: 0; right: 0; top: 32px; justify-content: center; }

  .name-tag {
    position: absolute;
    top: 14px; right: 40px;
    width: 150px; height: 44px;
    background: var(--sky);
    color: var(--white);
    text-align: right;
    padding: 5px 10px;
  }
  .name-tag__name { font-weight: 700; font-size: 13px; letter-spacing: .5px; display: block; }
  .name-tag__role { font-size: 11px; display: block; }

  .icon-box {
    position: absolute;
    width: 36px; height: 36px;
    background: var(--ocean);
    display: flex; align-items: center; justify-content: center;
  }
  .icon-box--phone { left: 70px; top: 212px; }
  .icon-box--social { right: 70px; top: 188px; }

  .website {
    position: absolute;
    left: 150px; top: 213px;
    font-weight: 700;
    font-size: 15px;
    color: var(--navy);
  }
  .phone {
    position: absolute;
    left: 54px; top: 262px;
    font-size: 12px;
    color: var(--white);
  }
  .social-handle {
    position: absolute;
    right: 40px; top: 246px;
    font-size: 12px;
    color: var(--white);
  }

  .services-title {
    position: absolute;
    left: 0; right: 0; top: 112px;
    text-align: center;
    font-size: 11px;
    letter-spacing: .5px;
    color: var(--ocean);
  }
  .service {
    position: absolute;
    width: 132px;
  }
  .service__photo {
    width: 132px; height: 86px;
    border: 3px solid var(--ocean);
  }
  .service__label {
    margin-top: 8px;
    font-size: 12px;
    color: var(--white);
    letter-spacing: .3px;
  }
  .service--minding { left: 36px; top: 108px; }
  .service--visits { left: 204px; top: 136px; }
  .service--walking { left: 372px; top: 172px; }
  .service--minding .service__photo { background: var(--photo-grass); }
  .service--visits .service__photo { background: var(--photo-door); }
  .service--walking .service__photo { background: var(--photo-park); }
</style>
</head>
<body>

  <section class="card card--front" aria-label="Business card front">
    <div class="band"></div>
    <div class="name-tag">
      <span class="name-tag__name">MARA LEESON</span>
      <span class="name-tag__role">Owner</span>
    </div>
    <div class="brand">
      <span class="brand__dot"></span>
      <span class="brand__name">Paws Harbour</span>
    </div>
    <span class="icon-box icon-box--social"></span>
    <p class="website">www.pawsharbourcare.example.au</p>
    <span class="icon-box icon-box--phone">
      <svg width="20" height="20" viewBox="0 0 24 24" aria-hidden="true">
        <path fill="#fff" d="M6.6 10.8a15.2 15.2 0 0 0 6.6 6.6l2.2-2.2a1 1 0 0 1 1-.25 11.4 11.4 0 0 0 3.6.6 1 1 0 0 1 1 1V20a1 1 0 0 1-1 1A17 17 0 0 1 3 4a1 1 0 0 1 1-1h3.5a1 1 0 0 1 1 1c0 1.25.2 2.45.6 3.6a1 1 0 0 1-.25 1z"/>
      </svg>
    </span>
    <p class="phone">0417 358 904</p>
    <p class="social-handle">pawsharbourcareau</p>
  </section>

  <section class="card card--back" aria-label="Business card back">
    <div class="band"></div>
    <div class="brand">
      <span class="brand__dot"></span>
      <span class="brand__name">Paws Harbour</span>
    </div>
    <p class="services-title">OUR THREE SERVICES</p>
    <div class="service service--minding">
      <div class="service__photo" role="img" aria-label="Photo of a dog resting on green grass"></div>
      <p class="service__label">DOG MINDING,</p>
    </div>
    <div class="service service--visits">
      <div class="service__photo" role="img" aria-label="Photo of a dog sitting on a home doormat"></div>
      <p class="service__label">HOME VISITS,</p>
    </div>
    <div class="service service--walking">
      <div class="service__photo" role="img" aria-label="Photo of a dog on a lead in a park"></div>
      <p class="service__label">DOG WALKING</p>
    </div>
  </section>

</body>
</html>
```